Uplift: Covid 19 (Poster)

We are looking to create a 11 by 17 inch 1 page poster.
-- Please Include NKR’s logo
-- Use the colors and font and mimic the feel of from Steady Step, Steady Breath Resource - Dementia Risk Reduction Flyers - Northern Council for Tribal Longevity (nkrcircle.org)
--> https://nkrcircle.org/resource-dementia-risk-reduction-flyers/
Moto needs to be included and it is: Protect Your Community. Protect Your Elders. Stay Vaccinated.
Include funding statement at the bottom of document - small print:
This project is supported by the Bureau for Illness Monitoring and Response of the U.S. Office of Wellness and Family Programs (OWFP) as part of a financial assistance award totaling $20,007,444 with 100 percent funded by BIMR/OWFP. The contents are those of the author(s) and do not necessarily represent the official views of, nor an endorsement, by BIMR/OWFP, or the U.S. Government.

```html
<!DOCTYPE html>
<html lang="en">
<head>
<meta charset="utf-8">
<title>Uplift – Fight COVID-19 Poster</title>
<link href="https://fonts.googleapis.com/css2?family=Montserrat:wght@400;600;700;800;900&display=swap" rel="stylesheet">
<style>
  :root {
    --sand: #f4e1c3;
    --sand-deep: #ead2ab;
    --teal: #4aa2ab;
    --teal-dark: #1f6c74;
    --brown: #5b2f0e;
    --wine: #a23b45;
    --band: #b9706c;
    --ink: #2a2a2a;
    --white: #ffffff;
  }
  * { margin: 0; padding: 0; box-sizing: border-box; }
  html, body { width: 776px; height: 1200px; overflow: hidden; background: var(--sand); }
  .poster {
    position: relative; width: 776px; height: 1200px; overflow: hidden;
    background: linear-gradient(180deg, var(--sand) 0%, var(--sand-deep) 50%, var(--sand) 100%);
    font-family: "Montserrat", sans-serif; color: var(--ink);
  }
  .title-box {
    position: absolute; left: 40px; top: 32px; width: 510px; height: 106px;
    border: 5px solid var(--white);
    display: flex; align-items: center; justify-content: center;
  }
  .title-box h1 {
    font-size: 84px; font-weight: 800; color: var(--teal); letter-spacing: 5px; line-height: 1;
  }
  .brand {
    position: absolute; left: 620px; top: 42px; display: flex; align-items: center; gap: 8px;
    font-size: 54px; font-weight: 800; color: var(--teal);
  }
  .brand .dot { width: 14px; height: 14px; background: var(--teal); border-radius: 50%; }
  .headline { position: absolute; left: 40px; top: 150px; color: var(--brown); font-weight: 900; line-height: 1; }
  .headline .line1 { font-size: 49px; letter-spacing: 1px; }
  .headline .line2 { font-size: 58px; margin-top: 6px; }
  .headline .accent { color: var(--wine); }
  .photo {
    position: absolute; left: 0; top: 262px; width: 776px; height: 420px;
    background: radial-gradient(ellipse at 30% 55%, #c9542c 0%, #8f3d27 35%, transparent 70%),
                radial-gradient(ellipse at 75% 60%, #5b3b7a 0%, #3b3566 30%, transparent 65%),
                linear-gradient(180deg, rgba(244,225,195,0) 0%, #b98f6e 45%, #7c5a48 100%);
  }
  .photo-caption {
    position: absolute; left: 0; width: 776px; top: 605px; text-align: center;
    font-size: 51px; font-weight: 800; color: var(--white);
  }
  .divider { position: absolute; left: 0; top: 680px; width: 776px; height: 22px; }
  .info { position: absolute; left: 73px; top: 730px; width: 640px; font-size: 12px; line-height: 14px; }
  .info .lead { color: var(--teal-dark); font-weight: 700; font-size: 13px; line-height: 17px; }
  .info ul { list-style: none; margin-top: 10px; }
  .info li { position: relative; padding-left: 11px; }
  .info li::before {
    content: ""; position: absolute; left: 1px; top: 5px; width: 5px; height: 5px;
    background: var(--teal-dark); transform: rotate(45deg);
  }
  .info .hl { font-weight: 700; color: var(--teal-dark); }
  .info .lead .hl { color: var(--wine); }
  .info .symptoms-lead { margin-top: 18px; }
  .info ul.symptoms { margin-top: 12px; }
  .cta {
    position: absolute; left: 0; width: 776px; top: 1048px; text-align: center;
    font-size: 56px; font-weight: 800; color: var(--teal-dark);
  }
  .cta .accent { color: var(--wine); }
  .funding {
    position: absolute; left: 0; top: 1108px; width: 776px; height: 84px; background: var(--band);
    color: var(--white); font-size: 11.2px; line-height: 13.5px; text-align: center;
    padding: 12px 60px;
  }
</style>
</head>
<body>
<main class="poster">
  <div class="title-box"><h1>UPLIFT</h1></div>
  <div class="brand"><span>NKR</span><span class="dot"></span></div>

  <header class="headline">
    <div class="line1">Protect Your Community</div>
    <div class="line2">Protect Your <span class="accent">Elders</span></div>
  </header>

  <div class="photo" role="img" aria-label="Photograph of three generations of Native women and children wrapped in colourful patterned blankets, wearing turquoise jewellery"></div>
  <div class="photo-caption">Stay Vaccinated</div>

  <svg class="divider" viewBox="0 0 776 22" aria-hidden="true">
    <rect x="0" y="0" width="776" height="22" fill="#f1dcc0" opacity="0.8"/>
    <line x1="0" y1="20" x2="776" y2="20" stroke="#e2c7a1" stroke-width="2"/>
  </svg>

  <section class="info">
    <p class="lead">American Indian and Alaska Native people have a higher risk of <span class="hl">COVID-19</span> infection rate than other population in the United States.</p>
    <ul>
      <li><span class="hl">COVID-19</span> is a virus that spreads mainly when infected people cough, sneeze, or talk.</li>
      <li>The best way to prevent yourself and others from <span class="hl">COVID-19</span> is by staying up to date with vaccination boosters.</li>
    </ul>
    <p class="lead symptoms-lead"><span class="hl">COVID-19 symptoms may take 2 to 14 days to appear after exposure to the virus,</span> and symptoms may include:</p>
    <ul class="symptoms">
      <li>Fever or chills</li>
      <li>Cough</li>
      <li>Shortness of breath or difficulty breathing</li>
      <li>Fatigue</li>
      <li>Muscle or body aches</li>
      <li>Headache</li>
      <li>New loss of taste or smell</li>
      <li>Sore throat</li>
      <li>Congestion or runny nose</li>
      <li>Nausea or vomiting</li>
      <li>Diarrhea</li>
    </ul>
  </section>

  <div class="cta">Fight <span class="accent">COVID-19!</span></div>

  <footer class="funding">
    This project is supported by the Bureau for Illness Monitoring and Response of the U.S. Office of Wellness and Family Programs (OWFP) as part of a financial assistance award totaling $20,007,444 with 100 percent funded by BIMR/OWFP. The contents are those of the author(s) and do not necessarily represent the official views of, nor an endorsement, by BIMR/OWFP, or the U.S. Government.
  </footer>
</main>
</body>
</html>
```